Business Card Design for Mabel's Pantry

We make food for dogs.
Business Card Design (using the logo designed by you). Our Brand color is a bright canary yellow. For example our signage is predominantly yellow, with the logo in black. I'd like the card also to use that imagery.
Feel free to use the two sides creatively.
Vertical Design is also great.

Industry/Entity Type

Pet food

Contact Information for Business Card

Name, email, website, phone no

Font styles to use
Sans Serif

Colors
59FF00
82FF00
B8FF75
E3FFCB
F4FFEA
FFF300
FFF600
FEFA6F
FFFEC7
FFFEE8

Requirements
Nice to have
• A graphic in the same brush stroke style of the logo shoeing a doggy bowl of food

```html
<!DOCTYPE html>
<html lang="en">
<head>
<meta charset="utf-8">
<title>Mabel's Pantry – Business Card</title>
<link href="https://fonts.googleapis.com/css2?family=Roboto:wght@400;500&display=swap" rel="stylesheet">
<style>
  :root {
    --backdrop: #959796;
    --card: #1b1b1b;
    --canary: #ffe25c;
    --white: #ffffff;
  }
  html, body {
    margin: 0;
    padding: 0;
    width: 1200px;
    height: 1200px;
    overflow: hidden;
    background: var(--backdrop);
    font-family: "Roboto", sans-serif;
  }
  .canvas { position: relative; width: 1200px; height: 1200px; }
  .card {
    position: absolute;
    background: var(--card);
  }
  .card--front { left: 69px; top: 174px; width: 487px; height: 853px; }
  .card--back { left: 655px; top: 176px; width: 486px; height: 850px; }
  .accent-stripe {
    position: absolute; left: 0; top: 0; width: 29px; height: 100%;
    background: var(--canary);
  }
  .brand-name {
    position: absolute;
    margin: 0;
    color: var(--canary);
    font-family: "Roboto", sans-serif;
    font-weight: 500;
    text-transform: uppercase;
    letter-spacing: 1px;
    white-space: nowrap;
    transform: translateX(-50%);
  }
  .card--front .brand-name { left: 243px; top: 214px; font-size: 36px; }
  .card--back .brand-name { left: 243px; top: 698px; font-size: 42px; }
  .holder { position: absolute; left: 54px; top: 568px; }
  .holder-name {
    margin: 0; color: var(--canary); font-size: 40px; font-weight: 400; line-height: 1;
  }
  .holder-role {
    margin: 6px 0 0; color: var(--white); font-size: 21px; line-height: 1;
  }
  .contacts {
    position: absolute; left: 54px; top: 684px;
    list-style: none; margin: 0; padding: 0;
  }
  .contact {
    display: flex; align-items: center; height: 35px;
    color: var(--white); font-size: 22px;
  }
  .contact-icon { width: 26px; height: 22px; margin-right: 12px; fill: none; stroke: var(--canary); stroke-width: 2; }
  .contact-icon .solid { fill: var(--canary); stroke: none; }
</style>
</head>
<body>
<main class="canvas">
  <section class="card card--front" aria-label="Card front">
    <div class="accent-stripe"></div>
    <h1 class="brand-name">Mabel's Pantry</h1>
    <div class="holder">
      <p class="holder-name">Dana Whitcombe</p>
      <p class="holder-role">Owner</p>
    </div>
    <ul class="contacts">
      <li class="contact">
        <svg class="contact-icon" viewBox="0 0 26 22" aria-hidden="true">
          <path class="solid" d="M2 8c0-3 5-5 11-5s11 2 11 5v2h-5V8c-2-1-10-1-12 0v2H2z"/>
          <path class="solid" d="M6 11h14l2 8H4z"/>
          <circle cx="13" cy="15" r="2.5" fill="#1b1b1b"/>
        </svg>
        555-014-2290
      </li>
      <li class="contact">
        <svg class="contact-icon" viewBox="0 0 26 22" aria-hidden="true">
          <rect class="solid" x="1" y="3" width="20" height="14"/>
          <path d="M1 3l10 8 10-8" stroke="#1b1b1b"/>
          <circle class="solid" cx="20" cy="16" r="5"/>
          <path d="M17.5 16l2 2 3-3.5" stroke="#1b1b1b" stroke-width="1.5"/>
        </svg>
        dana@mabelspantry.com
      </li>
      <li class="contact">
        <svg class="contact-icon" viewBox="0 0 26 22" aria-hidden="true">
          <circle cx="13" cy="11" r="9.5"/>
          <ellipse cx="13" cy="11" rx="4.5" ry="9.5"/>
          <path d="M3.5 11h19M5 6h16M5 16h16M13 1.5v19"/>
        </svg>
        www.MabelsPantry.com
      </li>
    </ul>
  </section>

  <section class="card card--back" aria-label="Card back">
    <p class="brand-name">Mabel's Pantry</p>
  </section>
</main>
</body>
</html>
```